Vista Clinic Needs a Web Design

Designers will use (and improve) our mockups to re-design our mobile-friendly website. We would like to see designs that use the color blue (as our logo in the attached file). The final design should convey convenience and communicate accessible health and wellness.

We need a web design for a company based in Kampala called 'Vista Clinic'.

We help patients to compare health insurance, find a doctor and book an appointment instantly.

Our initial products are Find and Book - a Wordpress database that helps patients to find a doctor and book an appointment instantly; and Insurance - a database that helps patients compare health insurance policies online. We would like to see designs that are mobile-friendly and responsive with awesome user interface and experience.
Updates

Project Deadline Extended Reason: We need web design of 5+ pages. Please see attached files for guidance. Added Wednesday, February 17, 2016

Industry/Entity Type

Health Service

Number of Pages Required

5+ page

Font styles to use
Sans Serif

Colors
33a6d7
85cae6
cee9f5
ecf7fb

Requirements
Must have
• Mobile-friendly and responsive design with awesome UI and UX

```html
<!DOCTYPE html>
<html lang="en">
<head>
<meta charset="utf-8">
<title>Vista Clinic – Find and Book</title>
<link rel="stylesheet" href="https://fonts.googleapis.com/css2?family=Roboto:wght@300;400;500;700&display=swap">
<style>
:root{
  --blue:#36c2ef;
  --blue-deep:#2aa9d6;
  --blue-soft:#85cae6;
  --ink:#111;
  --text:#2b2b2b;
  --muted:#555;
  --white:#fff;
  --rule:#d6d6d6;
  --dark:#2a2a2a;
}
*{box-sizing:border-box;margin:0;padding:0}
html,body{width:1200px;height:3383px;overflow:hidden}
body{font-family:"Roboto",Arial,sans-serif;color:var(--text);background:var(--white);position:relative}
section,header,footer{position:absolute;left:0;width:1200px;overflow:hidden}
.abs{position:absolute}
.btn{position:absolute;display:flex;align-items:center;justify-content:center;font-size:18px;font-weight:500;text-transform:uppercase;letter-spacing:.3px;border-radius:3px}
.btn-dark{background:var(--ink);color:var(--white)}
.btn-blue{background:var(--blue);color:var(--white)}

/* header */
.site-header{top:0;height:90px;background:var(--white)}
.nav-link{position:absolute;top:34px;font-size:15px;color:var(--ink);font-weight:500}
.brand{position:absolute;left:470px;top:24px;width:260px;height:42px;display:flex;align-items:center;gap:10px;font-size:25px;font-weight:700;color:var(--ink)}
.brand-dot{width:26px;height:26px;border-radius:50%;background:var(--blue)}
.insurance-tab{position:absolute;left:751px;top:25px;width:127px;height:36px;background:var(--blue);color:var(--white);font-size:15px;display:flex;align-items:center;justify-content:center}
.auth{position:absolute;left:911px;top:34px;font-size:15px;color:var(--ink)}
.auth span{color:var(--blue)}

/* hero */
.hero{top:90px;height:665px}
.hero-photo{position:absolute;inset:0;background:linear-gradient(120deg,#6fd3f3 0%,#45c3ee 45%,#35b4e2 100%)}
.hero-title{position:absolute;top:56px;width:100%;text-align:center;font-size:38px;font-weight:500;color:var(--white)}
.search{position:absolute;left:142px;top:151px;width:914px;height:70px;background:var(--white);display:flex;align-items:center}
.search-field{flex:1;display:flex;align-items:center;gap:14px;padding-left:22px;font-size:18px;color:#8a8a8a}
.search-btn{width:95px;height:70px;background:var(--ink);display:flex;align-items:center;justify-content:center}
.pill{position:absolute;top:289px;height:50px;background:var(--white);border-radius:25px;display:flex;align-items:center;justify-content:center;gap:12px;font-size:22px;font-weight:500;color:var(--ink)}
.speciality{position:absolute;top:402px;width:180px;text-align:center;color:var(--white)}
.speciality svg{display:block;margin:0 auto 24px}
.speciality span{font-size:17px}
.show-all{left:517px;top:562px;width:167px;height:36px;border-radius:18px;font-size:16px}
.dots{position:absolute;top:627px;left:0;width:100%;display:flex;justify-content:center;gap:9px}
.dots i{width:7px;height:7px;border-radius:50%;background:rgba(255,255,255,.6)}
.dots i:first-child{background:var(--white)}

/* app promo */
.app-promo{top:755px;height:408px}
.app-photo{position:absolute;inset:0;background:linear-gradient(90deg,#1c1c1c 0%,#3a3a3a 45%,#8a8a8a 80%,#b5b5b5 100%)}
.phone{position:absolute;border-radius:30px}
.phone-light{background:#e9e9e9;border:3px solid #cfcfcf}
.phone-dark{background:#1a1a1a;border:3px solid #3c3c3c}
.phone-screen{position:absolute;left:12px;right:12px;top:16%;bottom:16%;background:var(--white);display:flex;align-items:center;justify-content:center;font-size:16px;font-weight:700;color:var(--ink)}
.promo-title{position:absolute;left:519px;top:92px;font-size:46px;font-weight:500;color:var(--blue)}
.promo-sub{position:absolute;left:519px;top:148px;font-size:24px;font-weight:300;color:var(--white)}
.store-badge{position:absolute;top:303px;height:54px;width:154px;background:var(--ink);border:2px solid #888;border-radius:6px}

/* section headings */
.sec-title{position:absolute;left:142px;font-size:28px;color:var(--blue);font-weight:400}
.sec-sub{position:absolute;left:142px;font-size:19px}
.sec-icon{position:absolute;left:984px;width:70px;height:70px;display:flex;align-items:center;justify-content:center}
.rule{position:absolute;left:142px;width:912px;height:1px;background:var(--rule)}
.feature-circle{position:absolute;left:147px;width:76px;height:76px;border-radius:50%;background:var(--blue);display:flex;align-items:center;justify-content:center}
.feature-text{position:absolute;left:241px;font-size:18px;line-height:24px}

/* insurance */
.insurance{top:1163px;height:702px;background:var(--white)}
.insurance .sec-sub{color:var(--muted)}
.compare-lead{position:absolute;left:142px;top:190px;font-size:24px;color:var(--ink)}
.offer{position:absolute;left:786px;top:282px;width:256px;height:256px;border-radius:50%;background:var(--blue);color:var(--white);font-size:29px;line-height:32px;text-align:center;display:flex;align-items:center;justify-content:center;padding:0 24px;box-shadow:0 14px 24px rgba(0,0,0,.18)}

/* campaign */
.campaign{top:1865px;height:623px}
.campaign-photo{position:absolute;inset:0;background:linear-gradient(180deg,#f1f1f1 0%,#e7e7e7 60%,#dcdcdc 100%)}
.campaign .sec-sub{color:var(--ink)}
.campaign-lead{position:absolute;left:0;width:100%;top:176px;text-align:center;font-size:18px;line-height:26px;color:var(--ink)}
.cause{position:absolute;top:328px;display:flex;gap:20px;font-size:17px;line-height:24px;color:var(--ink)}
.vdivider{position:absolute;left:756px;top:290px;width:1px;height:280px;background:#cfcfcf}

/* schedule */
.schedule{top:2488px;height:787px}
.schedule-photo{position:absolute;inset:0;background:linear-gradient(160deg,#3a3a3a 0%,#2e2e2e 50%,#4a4a4a 100%)}
.schedule .sec-sub{color:var(--white)}
.schedule .rule{background:#777}
.schedule .feature-text{color:var(--white)}
.schedule-lead{position:absolute;top:156px;width:100%;text-align:center;font-size:18px;color:var(--white)}

/* footer */
.site-footer{top:3275px;height:108px;background:var(--white)}
.footer-links{position:absolute;left:142px;top:16px;font-size:14px;color:var(--ink)}
.copyright{position:absolute;left:142px;top:55px;font-size:14px;color:var(--ink)}
.social{position:absolute;left:993px;top:36px;display:flex;gap:12px}
.social i{width:12px;height:12px;border-radius:50%;background:#333}
</style>
</head>
<body>

<header class="site-header">
  <span class="nav-link" style="left:156px">VC For Doctors</span>
  <span class="nav-link" style="left:309px">Blog</span>
  <div class="brand"><span class="brand-dot"></span>vistaclinic</div>
  <div class="insurance-tab">Insurance</div>
  <div class="auth">Login &nbsp;|&nbsp; <span>Register</span></div>
</header>

<section class="hero">
  <div class="hero-photo" role="img" aria-label="Blue-tinted photo of a hand holding a smartphone"></div>
  <h1 class="hero-title">Find and Book</h1>
  <div class="search">
    <div class="search-field">
      <svg width="16" height="16" viewBox="0 0 16 16"><circle cx="6.5" cy="6.5" r="5" fill="none" stroke="#999" stroke-width="2"/><path d="M10 10l4.5 4.5" stroke="#999" stroke-width="2"/></svg>
      Specialities, Doctors, Clinics, Hospitals, Tests, etc
    </div>
    <div class="search-btn"><svg width="22" height="22" viewBox="0 0 16 16"><circle cx="6.5" cy="6.5" r="5" fill="none" stroke="#fff" stroke-width="2.2"/><path d="M10 10l4.5 4.5" stroke="#fff" stroke-width="2.4"/></svg></div>
  </div>
  <div class="pill" style="left:248px;width:235px">
    <svg width="26" height="22" viewBox="0 0 26 22"><rect x="1" y="5" width="24" height="16" rx="2" fill="var(--blue)"/><rect x="9" y="1" width="8" height="5" rx="1" fill="none" stroke="var(--blue)" stroke-width="2"/><path d="M13 9v8M9 13h8" stroke="#fff" stroke-width="2.4"/></svg>Doctors
  </div>
  <div class="pill" style="left:717px;width:233px">
    <svg width="14" height="26" viewBox="0 0 14 26"><rect x="3" y="1" width="8" height="23" rx="4" fill="none" stroke="var(--blue)" stroke-width="2"/><rect x="5" y="12" width="4" height="10" rx="2" fill="var(--blue)"/></svg>LabTests
  </div>

  <div class="speciality" style="left:129px">
    <svg width="34" height="40" viewBox="0 0 34 40"><path d="M4 4c5-5 10 0 13 0s8-5 13 0c4 5 1 13-1 17-2 5-2 17-6 17-3 0-3-12-6-12s-3 12-6 12c-4 0-4-12-6-17C3 17 0 9 4 4z" fill="#111"/></svg>
    <span>Dentist</span>
  </div>
  <div class="speciality" style="left:296px">
    <svg width="40" height="40" viewBox="0 0 40 40"><circle cx="20" cy="18" r="15" fill="#111"/><rect x="12" y="28" width="14" height="12" fill="#111"/></svg>
    <span>Dermatologist</span>
  </div>
  <div class="speciality" style="left:481px">
    <svg width="36" height="40" viewBox="0 0 36 34"><path d="M18 32C6 23 1 17 1 10 1 5 5 1 10 1c4 0 6 2 8 5 2-3 4-5 8-5 5 0 9 4 9 9 0 7-5 13-17 22z" fill="#111"/></svg>
    <span>Cardiologist</span>
  </div>
  <div class="speciality" style="left:673px">
    <svg width="30" height="40" viewBox="0 0 30 40"><path d="M15 2C7 2 2 8 2 15c0 5 3 7 5 10s1 8 6 12c4 3 9 0 9-4 0-5 6-9 6-18C28 8 23 2 15 2z" fill="#111"/><path d="M10 15c0-4 3-6 5-6s5 2 5 6" fill="none" stroke="#3fbde9" stroke-width="2.5"/></svg>
    <span>Ear Nose Throat</span>
  </div>
  <div class="speciality" style="left:851px">
    <svg width="30" height="40" viewBox="0 0 30 40"><path d="M2 2h10v22h14v14h-8v-8H8V10H2z" fill="#111"/></svg>
    <span>Psychiatrist</span>
  </div>
  <div class="btn btn-dark show-all">Show all</div>
  <div class="dots"><i></i><i></i><i></i><i></i></div>
</section>

<section class="app-promo">
  <div class="app-photo" role="img" aria-label="Dark photo of a doctor holding a clipboard"></div>
  <div class="phone phone-light" role="img" aria-label="Smartphone showing the Vista Clinic app" style="left:253px;top:18px;width:180px;height:370px">
    <div class="phone-screen">vistaclinic</div>
  </div>
  <h2 class="promo-title">Find A Doctor</h2>
  <p class="promo-sub">and book an appointment in Seconds</p>
  <div class="btn btn-blue" style="left:519px;top:220px;width:271px;height:38px;font-size:17px">Book an appointment</div>
  <div class="store-badge" style="left:519px"></div>
  <div class="store-badge" style="left:690px"></div>
</section>

<section class="insurance">
  <h2 class="sec-title" style="top:74px">Vista Clinic</h2>
  <p class="sec-sub" style="top:108px">Could Save Money</p>
  <div class="sec-icon" style="top:71px;background:var(--ink)">
    <svg width="24" height="40" viewBox="0 0 24 40"><path d="M12 2v36M20 10c-2-3-5-4-8-4-4 0-8 2-8 6 0 9 16 5 16 15 0 4-4 7-8 7-4 0-7-2-9-5" fill="none" stroke="#fff" stroke-width="3.5"/></svg>
  </div>
  <div class="rule" style="top:150px"></div>
  <p class="compare-lead">Compare Over 8 health Insurance Providers And get covered today !</p>

  <div class="feature-circle" style="top:263px"><svg width="32" height="28" viewBox="0 0 32 28"><path d="M2 14C2 6 6 2 13 2v5c-4 0-6 2-6 6h6v13H2zM19 14c0-8 4-12 11-12v5c-4 0-6 2-6 6h6v13H19z" fill="#fff"/></svg></div>
  <p class="feature-text" style="top:289px">Get a free, No obligation Health insurane quote</p>
  <div class="feature-circle" style="top:365px"><svg width="36" height="36" viewBox="0 0 36 36"><circle cx="18" cy="18" r="15" fill="none" stroke="#fff" stroke-width="3"/><circle cx="12.5" cy="14" r="2" fill="#fff"/><circle cx="23.5" cy="14" r="2" fill="#fff"/><path d="M11 21c3 5 11 5 14 0" fill="none" stroke="#fff" stroke-width="3"/></svg></div>
  <p class="feature-text" style="top:391px">Simple and jargan free</p>
  <div class="feature-circle" style="top:473px"><svg width="38" height="26" viewBox="0 0 38 26"><rect x="2" y="2" width="34" height="22" fill="none" stroke="#fff" stroke-width="3"/><circle cx="19" cy="13" r="5" fill="#fff"/></svg></div>
  <p class="feature-text" style="top:499px">Low Monthly Payments</p>

  <div class="offer">Take care of your loved ones from UGX 30,000 a month</div>
  <div class="btn btn-dark" style="left:481px;top:604px;width:236px;height:42px">Compare now!</div>
</section>

<section class="campaign">
  <div class="campaign-photo" role="img" aria-label="Faded grey photo of a medical professional with health icons"></div>
  <h2 class="sec-title" style="top:40px">Vista Clinic</h2>
  <p class="sec-sub" style="top:74px">Saves you worry</p>
  <div class="sec-icon" style="top:35px;width:67px;height:67px;background:var(--ink)">
    <svg width="26" height="34" viewBox="0 0 26 34"><rect x="2" y="4" width="22" height="29" fill="#fff"/><path d="M11 0h4v8h-4z" fill="#fff"/><path d="M7 11h4v4H7zM15 11h4v4h-4zM7 19h4v4H7zM15 19h4v4h-4zM10 27h6v6h-6z" fill="#111"/></svg>
  </div>
  <div class="rule" style="top:113px"></div>
  <p class="campaign-lead">Worry. It never feels good. We'd rather you experience more enjoyable emotions like<br>happiness.raise funds for your medical cause</p>
  <div class="rule" style="top:274px"></div>
  <div class="vdivider"></div>

  <div class="cause" style="left:156px"><svg width="28" height="28" viewBox="0 0 28 28"><rect width="28" height="28" rx="4" fill="var(--blue)"/><path d="M8 20l1-4 9-9 3 3-9 9z" fill="#fff"/></svg><span>Create a campaign<br>to raise funds for<br>your medical cause</span></div>
  <div class="cause" style="left:465px"><svg width="32" height="24" viewBox="0 0 32 24"><rect x="1" y="1" width="30" height="22" rx="2" fill="none" stroke="var(--blue)" stroke-width="2.5"/><rect x="1" y="6" width="30" height="4" fill="var(--blue)"/><rect x="5" y="15" width="8" height="3" fill="var(--blue)"/></svg><span>Receive donations to<br>your cause direct to<br>your acount</span></div>
  <div class="cause" style="left:781px"><svg width="28" height="28" viewBox="0 0 28 28"><rect x="2" y="10" width="24" height="16" fill="var(--blue)"/><rect x="0" y="7" width="28" height="5" fill="var(--blue)"/><path d="M13 7h2v19h-2z" fill="#fff"/><path d="M14 7C10 1 5 3 8 7M14 7c4-6 9-4 6 0" fill="none" stroke="var(--blue)" stroke-width="2"/></svg><span>Support any cause<br>or campaign you<br>like</span></div>

  <div class="btn btn-dark" style="left:325px;top:468px;width:237px;height:41px">Start a campaign</div>
  <div class="btn btn-dark" style="left:794px;top:468px;width:237px;height:41px">Donate</div>
</section>

<section class="schedule">
  <div class="schedule-photo" role="img" aria-label="Dark photo of a person working on a laptop"></div>
  <h2 class="sec-title" style="top:48px">Vista Clinic</h2>
  <p class="sec-sub" style="top:83px">Saves you worry</p>
  <div class="sec-icon" style="top:41px;width:68px;height:68px;background:var(--blue)">
    <svg width="34" height="34" viewBox="0 0 34 34"><circle cx="17" cy="17" r="14" fill="none" stroke="#fff" stroke-width="3"/><path d="M17 9v9h7" fill="none" stroke="#fff" stroke-width="3"/></svg>
  </div>
  <div class="rule" style="top:122px"></div>
  <p class="schedule-lead">We know you don't want to spend all your time waiting in line</p>

  <div class="feature-circle" style="top:265px"><svg width="32" height="32" viewBox="0 0 32 32"><rect x="2" y="5" width="28" height="25" rx="2" fill="#fff"/><rect x="2" y="5" width="28" height="7" fill="#d9f3fc"/><path d="M9 1v8M23 1v8" stroke="#fff" stroke-width="3"/><path d="M7 16h4v4H7zM14 16h4v4h-4zM21 16h4v4h-4zM7 23h4v4H7zM14 23h4v4h-4z" fill="var(--blue)"/></svg></div>
  <p class="feature-text" style="top:291px">See Doctor's Schedule</p>
  <div class="feature-circle" style="top:371px"><svg width="34" height="28" viewBox="0 0 34 28"><rect x="1" y="6" width="32" height="21" rx="2" fill="#fff"/><rect x="11" y="1" width="12" height="6" rx="1" fill="none" stroke="#fff" stroke-width="2.5"/><rect x="1" y="14" width="32" height="2" fill="var(--blue)"/></svg></div>
  <p class="feature-text" style="top:397px">Choose a time that works for you</p>
  <div class="feature-circle" style="top:475px"><svg width="30" height="32" viewBox="0 0 30 32"><path d="M4 2h22v24H7a3 3 0 0 0 0 6h19" fill="#fff" stroke="#fff" stroke-width="2"/><path d="M9 9h12M9 14h12" stroke="var(--blue)" stroke-width="2.5"/></svg></div>
  <p class="feature-text" style="top:489px">Book Instantly. No phone Calls<br>No waiting on hold</p>

  <div class="phone phone-dark" role="img" aria-label="Smartphone showing the Vista Clinic app" style="left:749px;top:215px;width:205px;height:428px">
    <div class="phone-screen">vistaclinic</div>
  </div>
  <div class="btn btn-blue" style="left:429px;top:677px;width:340px;height:43px;font-size:17px">Book an appointment now</div>
</section>

<footer class="site-footer">
  <p class="footer-links">About &nbsp;|&nbsp; Contact Us &nbsp;|&nbsp; Privacy &amp; Terms</p>
  <p class="copyright">Copyright ©2016 Vista Clinic Limited. All Rights Reserved</p>
  <div class="social"><i></i><i></i><i></i></div>
</footer>

</body>
</html>
```